Wordpress Design Project

we need a functional wordpress template for a review site.

This site will work predominantly for consumers wishing to make a comment on services.

This is a new site, and will be launched through social media.

The design should communicate a feeling of trust and where they can tell their feelings to the world. It should be one that looks professional and not like a gossip site, but also needs to have elements of colour and fun to keep Gen Y interested.

the site must look legitimate.
Updates

Target Market(s)

25-45 males and females in the workplace

Industry/Entity Type

Media

Requirements
Must have
• template must be quite simple and easily manipulated.

www.roamverdict.example
www.thewhirl.example.au
www.mvbrightharbour.example.au

it must be easy to use, with bold colours. must be modern.

```html
<!DOCTYPE html>
<html lang="en">
<head>
<meta charset="utf-8">
<title>Candorly — Ratings You Can Trust</title>
<link rel="stylesheet" href="https://fonts.googleapis.com/css2?family=Open+Sans:wght@400;700&family=Sorts+Mill+Goudy:ital@0;1&family=Lora:ital,wght@1,400;1,600&display=swap">
<style>
:root{
  --header-top:#2a2a2a;
  --header-bottom:#0f0f0f;
  --page-bg:#efefef;
  --line:#d2d2d2;
  --text-dark:#3a3a3a;
  --text-body:#5a5a5a;
  --text-muted:#a8a8a8;
  --meta-name:#6a6a6a;
  --nav-text:#f2f2f2;
  --nav-active:#7cc4ec;
  --photo:#d0d0d0;
  --frame:#fbfbfb;
  --green-top:#7ea95e;
  --green-bottom:#5a873c;
  --ribbon:#5ea9b9;
  --ribbon-dark:#3b7c8a;
  --star:#f6b21a;
  --star-off:#dcdcdc;
}
*{box-sizing:border-box;margin:0;padding:0}
html,body{width:1200px;height:900px;overflow:hidden}
body{position:relative;background:var(--page-bg);font-family:"Open Sans",sans-serif;color:var(--text-body)}
.abs{position:absolute}

/* header */
.site-header{position:absolute;left:0;top:0;width:1200px;height:66px;background:linear-gradient(var(--header-top),var(--header-bottom))}
.site-header::after{content:"";position:absolute;left:558px;top:66px;border:7px solid transparent;border-top-color:#151515;border-bottom:0}
.brand{position:absolute;left:90px;top:17px;font:400 24px/30px "Sorts Mill Goudy",serif;color:#fff}
.tagline{position:absolute;left:202px;top:25px;font:italic 13px/18px "Lora",serif;color:#9a9a9a}
.main-nav{position:absolute;top:21px;left:550px;width:436px;display:flex;justify-content:space-between}
.main-nav a,.footer-nav a{font:italic 14px/20px "Lora",serif;color:var(--nav-text);text-decoration:none;white-space:nowrap}
.main-nav a.active,.footer-nav a.active{color:var(--nav-active)}

/* section title */
.section-rule{position:absolute;left:65px;width:963px;height:1px;background:var(--line);box-shadow:0 1px 0 #fff}
.section-tab{position:absolute;left:472px;top:95px;width:178px;height:37px;background:linear-gradient(#fff,#f3f3f3);border-radius:6px 6px 0 0;box-shadow:0 -1px 2px rgba(0,0,0,.12);text-align:center;font:400 19px/36px "Sorts Mill Goudy",serif;color:var(--text-muted);text-transform:uppercase}

/* photo frames */
.photo-frame{position:absolute;background:var(--frame);border:1px solid #e0e0e0;box-shadow:0 1px 2px rgba(0,0,0,.06)}
.photo{position:absolute;background:var(--photo);box-shadow:inset 0 0 0 2px #a9a9a9,inset 0 3px 6px rgba(0,0,0,.2)}

/* feature */
.feature-title{position:absolute;left:516px;top:182px;font:400 26px/34px "Sorts Mill Goudy",serif;color:var(--text-dark)}
.meta{font:italic 13px/16px "Sorts Mill Goudy",serif;color:var(--text-muted)}
.meta b{font-weight:400;color:var(--meta-name)}
.rating-pill{position:absolute;top:242px;height:26px;background:#fff;border:1px solid #dedede;border-radius:7px;display:flex;align-items:center;padding-left:11px;gap:7px;font:italic 13px/1 "Lora",serif;color:#333}
.stars{display:flex;gap:1px}
.stars svg{width:14px;height:14px}
.excerpt{position:absolute;left:517px;top:273px;width:450px;font-size:11px;line-height:22px;color:var(--text-body)}
.arrow{position:absolute;top:268px;width:26px;height:38px}

/* buttons */
.btn{position:absolute;height:31px;border-radius:16px;background:linear-gradient(var(--green-top),var(--green-bottom));border:1px solid #4d7632;box-shadow:0 2px 3px rgba(0,0,0,.25),inset 0 1px 0 rgba(255,255,255,.25);color:#fff;text-align:center;font:400 17px/29px "Sorts Mill Goudy",serif;text-shadow:0 1px 1px rgba(0,0,0,.3);text-decoration:none}

/* cards */
.card{position:absolute;top:502px;width:263px;height:240px;background:var(--frame);border:1px solid #e2e2e2}
.card .photo{left:8px;top:8px;width:245px;height:130px}
.card .ribbon{position:absolute;right:-11px;top:-12px;width:99px;height:99px;overflow:visible}
.card .star-badge{position:absolute;left:81px;top:125px;width:101px;height:27px;background:#fff;border:1px solid #dcdcdc;border-radius:7px;display:flex;justify-content:center;align-items:center}
.card-title{position:absolute;left:0;top:160px;width:100%;text-align:center;font:400 26px/34px "Sorts Mill Goudy",serif;color:var(--text-dark)}
.card .meta{position:absolute;left:0;top:195px;width:100%;text-align:center;font-size:12px}
.card .btn{left:75px;top:223px;width:114px}

/* footer */
.footer-band{position:absolute;left:0;top:805px;width:1200px;height:36px;background:linear-gradient(#262626,#161616);border-top:1px solid #0a0a0a}
.site-footer{position:absolute;left:0;top:841px;width:1200px;height:59px;background:linear-gradient(#1d1d1d,#111)}
.footer-nav{position:absolute;left:87px;top:24px;width:467px;display:flex;justify-content:space-between}
.footer-nav a{font-weight:600}
</style>
</head>
<body>
<svg width="0" height="0" style="position:absolute">
  <defs>
    <symbol id="star" viewBox="0 0 20 20"><path d="M10 1l2.7 5.8 6.3.7-4.7 4.3 1.3 6.2L10 14.9 4.4 18l1.3-6.2L1 7.5l6.3-.7z"/></symbol>
    <linearGradient id="half"><stop offset="50%" stop-color="#f6b21a"/><stop offset="50%" stop-color="#dcdcdc"/></linearGradient>
  </defs>
</svg>

<header class="site-header">
  <div class="brand">Candorly</div>
  <div class="tagline">Ratings You Can Trust</div>
  <nav class="main-nav">
    <a class="active">Home</a>
    <a>About</a>
    <a>Categories</a>
    <a>Page Title</a>
    <a>Page Title2</a>
    <a>Blog</a>
    <a>Contact Us</a>
  </nav>
</header>

<main>
  <div class="section-rule" style="top:131px"></div>
  <h2 class="section-tab">Title Here</h2>

  <section class="featured-review">
    <svg class="arrow" style="left:66px" viewBox="0 0 26 38"><path d="M20 4L6 19l14 15" fill="none" stroke="#fff" stroke-width="7" stroke-linecap="round" stroke-linejoin="round"/><path d="M20 4L6 19l14 15" fill="none" stroke="#9a9a9a" stroke-width="2" stroke-linecap="round" stroke-linejoin="round"/></svg>
    <svg class="arrow" style="left:1000px" viewBox="0 0 26 38"><path d="M6 4l14 15L6 34" fill="none" stroke="#fff" stroke-width="7" stroke-linecap="round" stroke-linejoin="round"/><path d="M6 4l14 15L6 34" fill="none" stroke="#9a9a9a" stroke-width="2" stroke-linecap="round" stroke-linejoin="round"/></svg>

    <div class="photo-frame" style="left:140px;top:170px;width:337px;height:221px">
      <div class="photo" role="img" aria-label="Featured review photo" style="left:7px;top:7px;width:321px;height:205px"></div>
    </div>

    <h1 class="feature-title">Post Title Goes Here</h1>
    <p class="meta abs" style="left:517px;top:217px">Reviewed by <b>Admin</b> on January 13, 2012</p>

    <div class="rating-pill" style="left:516px;width:145px">Author
      <span class="stars">
        <svg fill="#f6b21a"><use href="#star"/></svg><svg fill="#f6b21a"><use href="#star"/></svg><svg fill="url(#half)"><use href="#star"/></svg><svg fill="#dcdcdc"><use href="#star"/></svg><svg fill="#dcdcdc"><use href="#star"/></svg>
      </span>
    </div>
    <div class="rating-pill" style="left:666px;width:137px">Users
      <span class="stars">
        <svg fill="#f6b21a"><use href="#star"/></svg><svg fill="#f6b21a"><use href="#star"/></svg><svg fill="#f6b21a"><use href="#star"/></svg><svg fill="#f6b21a"><use href="#star"/></svg><svg fill="#f6b21a"><use href="#star"/></svg>
      </span>
    </div>

    <p class="excerpt">Pellentesque tempor dui non mauris ullamcorper sit amet mattis metus dapibus. Vestibulum ante ipsum primis in faucibus orci luctus et ultrices posuere cubilia Curae; Nullam tristique faucibus gravida. Donec vitae placerat nunc. Nunc ornare odio at augue viverra non fermentum quam imperdiet. Donec molestie commodo faucibus. Mauris</p>

    <div class="section-rule" style="top:431px"></div>
    <a class="btn" style="left:450px;top:415px;width:243px">Click to Read The Full Review</a>
  </section>

  <section class="review-cards">
    <article class="card" style="left:97px">
      <div class="photo" role="img" aria-label="Review photo"></div>
      <svg class="ribbon" viewBox="0 0 99 99"><path d="M0 0h27l72 72v27z" fill="var(--ribbon)"/><path d="M88 88l11 0 0 11z" fill="var(--ribbon-dark)"/><text x="47" y="45" transform="rotate(45 50 50)" text-anchor="middle" font-family="Open Sans,sans-serif" font-size="10" fill="#fff">editor's choice</text></svg>
      <div class="star-badge"><span class="stars"><svg fill="#f6b21a"><use href="#star"/></svg><svg fill="#f6b21a"><use href="#star"/></svg><svg fill="#f6b21a"><use href="#star"/></svg><svg fill="#dcdcdc"><use href="#star"/></svg><svg fill="#dcdcdc"><use href="#star"/></svg></span></div>
      <h3 class="card-title">Post Title Goes Here</h3>
      <p class="meta">Reviewed by <b>Admin</b> on January 17,2012</p>
      <a class="btn">Full Review</a>
    </article>
    <article class="card" style="left:457px">
      <div class="photo" role="img" aria-label="Review photo"></div>
      <svg class="ribbon" viewBox="0 0 99 99"><path d="M0 0h27l72 72v27z" fill="var(--ribbon)"/><path d="M88 88l11 0 0 11z" fill="var(--ribbon-dark)"/><text x="47" y="45" transform="rotate(45 50 50)" text-anchor="middle" font-family="Open Sans,sans-serif" font-size="10" fill="#fff">editor's choice</text></svg>
      <div class="star-badge"><span class="stars"><svg fill="#f6b21a"><use href="#star"/></svg><svg fill="#f6b21a"><use href="#star"/></svg><svg fill="#f6b21a"><use href="#star"/></svg><svg fill="#dcdcdc"><use href="#star"/></svg><svg fill="#dcdcdc"><use href="#star"/></svg></span></div>
      <h3 class="card-title">Post Title Goes Here</h3>
      <p class="meta">Reviewed by <b>Admin</b> on January 17,2012</p>
      <a class="btn">Full Review</a>
    </article>
    <article class="card" style="left:807px">
      <div class="photo" role="img" aria-label="Review photo"></div>
      <svg class="ribbon" viewBox="0 0 99 99"><path d="M0 0h27l72 72v27z" fill="var(--ribbon)"/><path d="M88 88l11 0 0 11z" fill="var(--ribbon-dark)"/><text x="47" y="45" transform="rotate(45 50 50)" text-anchor="middle" font-family="Open Sans,sans-serif" font-size="10" fill="#fff">editor's choice</text></svg>
      <div class="star-badge"><span class="stars"><svg fill="#f6b21a"><use href="#star"/></svg><svg fill="#f6b21a"><use href="#star"/></svg><svg fill="#f6b21a"><use href="#star"/></svg><svg fill="#dcdcdc"><use href="#star"/></svg><svg fill="#dcdcdc"><use href="#star"/></svg></span></div>
      <h3 class="card-title">Post Title Goes Here</h3>
      <p class="meta">Reviewed by <b>Admin</b> on January 17,2012</p>
      <a class="btn">Full Review</a>
    </article>
  </section>
</main>

<div class="footer-band"></div>
<footer class="site-footer">
  <nav class="footer-nav">
    <a class="active">Home</a>
    <a>About</a>
    <a>Categories</a>
    <a>Page Title</a>
    <a>Page Title2</a>
    <a>Blog</a>
    <a>Contact Us</a>
  </nav>
</footer>
</body>
</html>
```